business card design

i would like business cards designed. My business provides trade qualified personnel to the mining industry to work on heavy mobile equipment.
please put a excavator(digger) in the background in one design and have one design without so i can compare the difference.
also add info:
my logo(attached) and "mobile equipment repair and maintenance"
name: Derek Holloway
address: 57 Tarrowby RD Kelvale Ridge WA.
mobile: 0438120957
email: derek@ironvalemx.com

```html
<!DOCTYPE html>
<html lang="en">
<head>
<meta charset="utf-8">
<title>Ironvale Maintenance Services – Business Cards</title>
<link rel="stylesheet" href="https://fonts.googleapis.com/css2?family=Montserrat:wght@400;500;700;800&display=swap">
<style>
  :root {
    --backdrop: #e9eaec;
    --navy: #0b1f45;
    --navy-deep: #071a3d;
    --accent-blue: #3d68bd;
    --tagline-blue: #4a72c4;
    --paper: #f1eff3;
    --body-text: #454548;
    --white: #ffffff;
  }
  * { box-sizing: border-box; margin: 0; padding: 0; }
  html, body {
    width: 1200px;
    height: 900px;
    overflow: hidden;
  }
  body {
    background: var(--backdrop);
    font-family: "Montserrat", Arial, sans-serif;
    position: relative;
  }
  .card {
    position: absolute;
    left: 379px;
    width: 443px;
    height: 271px;
  }
  .card--front {
    top: 145px;
    background: radial-gradient(ellipse at 50% 45%, #0a2249 0%, var(--navy-deep) 75%);
    color: var(--white);
  }
  .card--back {
    top: 484px;
    background: var(--paper);
    color: var(--navy);
  }

  /* Company name block */
  .company-name {
    font-weight: 800;
    line-height: 1;
    text-transform: uppercase;
  }
  .company-name__main {
    display: block;
    font-size: 36px;
    letter-spacing: 5px;
  }
  .company-name__sub {
    display: block;
    font-size: 9.6px;
    letter-spacing: 1.3px;
    margin-top: 7px;
  }
  .card--front .company-name {
    position: absolute;
    top: 113px;
    left: 0;
    right: 0;
    text-align: center;
    color: var(--white);
  }
  .card--back .company-name {
    position: absolute;
    top: 26px;
    left: 27px;
    color: var(--navy);
  }
  .card--back .company-name__sub { padding-left: 2px; }

  .tagline {
    position: absolute;
    top: 231px;
    left: 0;
    right: 0;
    text-align: center;
    font-size: 10.4px;
    font-weight: 500;
    color: var(--tagline-blue);
    letter-spacing: 0.3px;
  }

  .person-name {
    position: absolute;
    top: 143px;
    right: 27px;
    font-size: 14px;
    font-weight: 700;
    letter-spacing: 0.4px;
    color: var(--navy);
    text-transform: uppercase;
  }
  .divider {
    position: absolute;
    top: 168px;
    left: 27px;
    right: 27px;
    height: 1.5px;
    background: var(--accent-blue);
  }
  .address {
    position: absolute;
    top: 179px;
    left: 27px;
    font-size: 10.4px;
    line-height: 14px;
    color: var(--body-text);
    font-style: normal;
  }
  .contact-list {
    position: absolute;
    top: 216px;
    left: 27px;
    list-style: none;
    font-size: 10.4px;
    line-height: 14px;
    color: var(--body-text);
  }
  .contact-list__item {
    display: flex;
    align-items: center;
    gap: 6px;
  }
  .contact-list__icon {
    width: 9px;
    height: 9px;
    flex: none;
    fill: var(--accent-blue);
  }
</style>
</head>
<body>

  <section class="card card--front" aria-label="Business card front">
    <h1 class="company-name">
      <span class="company-name__main">Ironvale</span>
      <span class="company-name__sub">Maintenance Services Pty Ltd</span>
    </h1>
    <p class="tagline">Mobile equipment repair and maintenance</p>
  </section>

  <section class="card card--back" aria-label="Business card back">
    <h2 class="company-name">
      <span class="company-name__main">Ironvale</span>
      <span class="company-name__sub">Maintenance Services Pty Ltd</span>
    </h2>
    <p class="person-name">Derek Holloway</p>
    <div class="divider"></div>
    <address class="address">
      57 Tarrowby RD<br>
      Kelvale Ridge WA
    </address>
    <ul class="contact-list">
      <li class="contact-list__item">
        <svg class="contact-list__icon" viewBox="0 0 24 24" aria-hidden="true">
          <path d="M6.6 10.8c1.4 2.8 3.8 5.1 6.6 6.6l2.2-2.2c.3-.3.7-.4 1-.2 1.1.4 2.300.6 3.6.6.6 0 1 .4 1 1V20c0 .6-.4 1-1 1C10.6 21 3 13.4 3 4c0-.6.4-1 1-1h3.5c.6 0 1 .4 1 1 0 1.3.2 2.5.6 3.6.1.3 0 .7-.2 1l-2.3 2.2z"/>
        </svg>
        <span>0438120957</span>
      </li>
      <li class="contact-list__item">
        <svg class="contact-list__icon" viewBox="0 0 24 24" aria-hidden="true">
          <path d="M2 5h20v14H2V5zm2 2v.5l8 5 8-5V7H4zm0 2.8V17h16V9.8l-8 5-8-5z"/>
        </svg>
        <span>derek@ironvalemx.com</span>
      </li>
    </ul>
  </section>

</body>
</html>
```